BQL Groundworks & Freight Business Card

Can you please design a business card for an Earthworks, Haulage truck and machinery hire company. They also provide sand soil and mulch supply, as well as screening of products. Can you re-create the logo from the attached but add BQL Groundworks & Freight just use the three diamond design.

Target Market(s)

Earthmoving and Transport, Landscapers, Construction

Contact Information for Business Card

ABN 52 907 334 816, Doug Pelham, Managing Director, BQL Groundworks & Freight Mobile 0438 256 904 Email bqlfreight2010@mailvane.net

Font styles to use
Sans Serif

Colors
ec1f27
000000
cbcbcb
ffffff

Requirements
Must have
• Listed on the back, Earthworks | Haulage | Truck and Machinery Hire | Sand, Soil & Mulch Supply | Screening of Products
Nice to have
• Would be good for it to look appealing to a mans man, because it relates to heavy machinery, earthworks, construction etc. Black, red and white would be good maybe with a bit of silver somewhere.
Should not have
• not sure

```html
<!DOCTYPE html>
<html lang="en">
<head>
<meta charset="UTF-8">
<title>BQL Groundworks &amp; Freight Business Card</title>
<link href="https://fonts.googleapis.com/css2?family=Montserrat:ital,wght@0,500;0,600;0,700;1,500;1,700&display=swap" rel="stylesheet">
<style>
  :root {
    --stage: #262626;
    --card: #141414;
    --accent: #dcdc4e;
  }
  * { box-sizing: border-box; margin: 0; padding: 0; }
  html, body { width: 1200px; height: 900px; overflow: hidden; }
  body {
    background: var(--stage);
    font-family: "Montserrat", sans-serif;
    color: var(--accent);
    display: flex;
    flex-direction: column;
    align-items: center;
    justify-content: center;
    gap: 40px;
  }
  .card {
    width: 700px;
    height: 400px;
    background: var(--card);
    position: relative;
    box-shadow: 0 14px 30px rgba(0,0,0,.45);
  }

  /* shared brand name */
  .brand-mark {
    display: flex;
    align-items: center;
    gap: 14px;
    font-weight: 700;
    color: var(--accent);
    line-height: 1;
  }
  .brand-mark .dot {
    border-radius: 50%;
    background: var(--accent);
  }

  /* back side */
  .card-back {
    display: flex;
    flex-direction: column;
    align-items: center;
    padding-top: 58px;
  }
  .card-back .brand-mark { font-size: 64px; }
  .card-back .brand-mark .dot { width: 56px; height: 56px; }
  .card-back .tagline {
    margin-top: 34px;
    font-size: 26px;
    font-weight: 600;
    letter-spacing: .3px;
  }
  .card-back .rule {
    width: 416px;
    height: 5px;
    background: var(--accent);
    margin-top: 10px;
  }
  .services {
    margin-top: 14px;
    font-size: 15px;
    font-weight: 600;
    text-align: center;
    line-height: 1.4;
  }

  /* front side */
  .person {
    position: absolute;
    left: 56px;
    top: 36px;
  }
  .person-name {
    font-size: 34px;
    font-weight: 700;
    font-style: italic;
    line-height: 1.1;
  }
  .person-role {
    font-size: 15px;
    font-weight: 500;
    font-style: italic;
    margin-top: 2px;
  }
  .person .rule {
    width: 270px;
    height: 5px;
    background: var(--accent);
    margin-top: 14px;
  }
  .service-icons {
    position: absolute;
    left: 50px;
    top: 208px;
    height: 50px;
    display: flex;
    gap: 28px;
    align-items: center;
  }
  .service-icons svg { display: block; }
  .icon-placeholder {
    height: 48px;
    background: var(--accent);
  }
  .icon-worker { width: 48px; border-radius: 50%; }
  .icon-crane { width: 60px; border-radius: 8px; }

  .front-brand {
    position: absolute;
    right: 64px;
    top: 78px;
    display: flex;
    flex-direction: column;
    align-items: center;
  }
  .front-brand .brand-mark { font-size: 52px; }
  .front-brand .brand-mark .dot { width: 44px; height: 44px; }
  .front-brand .tagline {
    margin-top: 30px;
    font-size: 21px;
    font-weight: 600;
  }
  .front-rule {
    position: absolute;
    left: 36px;
    right: 36px;
    top: 270px;
    height: 2px;
    background: var(--accent);
  }
  .contacts {
    position: absolute;
    left: 40px;
    top: 282px;
    list-style: none;
    font-size: 20px;
    font-weight: 500;
    font-style: italic;
    line-height: 1.45;
  }
  .contacts li { display: flex; align-items: center; gap: 14px; }
  .contacts svg { width: 18px; height: 18px; flex: none; }
</style>
</head>
<body>

  <section class="card card-back">
    <div class="brand-mark"><span class="dot"></span>BQL</div>
    <p class="tagline">Groundworks &amp; Freight</p>
    <div class="rule"></div>
    <p class="services">
      Earthworks | Haulage | Truck and Machinery Hire |<br>
      Sand, Soil &amp; Mulch Supply | Screening of Products
    </p>
  </section>

  <section class="card card-front">
    <div class="person">
      <h1 class="person-name">Doug Pelham</h1>
      <p class="person-role">Managing Director</p>
      <div class="rule"></div>
    </div>

    <div class="service-icons">
      <svg width="56" height="44" viewBox="0 0 56 44" aria-label="Haulage truck">
        <rect x="2" y="4" width="34" height="28" rx="3" fill="var(--accent)"/>
        <path d="M36 12h10l8 10v10H36z" fill="var(--accent)"/>
        <circle cx="12" cy="36" r="6" fill="var(--accent)" stroke="var(--card)" stroke-width="2"/>
        <circle cx="44" cy="36" r="6" fill="var(--accent)" stroke="var(--card)" stroke-width="2"/>
      </svg>
      <div class="icon-placeholder icon-worker" role="img" aria-label="Worker digging icon"></div>
      <div class="icon-placeholder icon-crane" role="img" aria-label="Crane truck icon"></div>
    </div>

    <div class="front-brand">
      <div class="brand-mark"><span class="dot"></span>BQL</div>
      <p class="tagline">Groundworks &amp; Freight</p>
    </div>

    <div class="front-rule"></div>

    <ul class="contacts">
      <li>
        <svg viewBox="0 0 24 24" aria-hidden="true"><path fill="var(--accent)" d="M6.6 10.8a15 15 0 0 0 6.6 6.6l2.2-2.2c.3-.3.7-.4 1-.2 1.1.4 2.3.6 3.6.6.6 0 1 .4 1 1V20c0 .6-.4 1-1 1A17 17 0 0 1 3 4c0-.6.4-1 1-1h3.5c.6 0 1 .4 1 1 0 1.3.2 2.5.6 3.6.1.3 0 .7-.2 1z"/></svg>
        0438 256 904
      </li>
      <li>
        <svg viewBox="0 0 24 24" aria-hidden="true"><circle cx="12" cy="12" r="9" fill="none" stroke="var(--accent)" stroke-width="3"/><circle cx="12" cy="12" r="3" fill="var(--accent)"/></svg>
        ABN 52 907 334 816
      </li>
      <li>
        <svg viewBox="0 0 24 24" aria-hidden="true"><rect x="2" y="5" width="20" height="14" fill="none" stroke="var(--accent)" stroke-width="2"/><path d="M2 5l10 8 10-8" fill="none" stroke="var(--accent)" stroke-width="2"/></svg>
        bqlfreight2010@mailvane.net
      </li>
    </ul>
  </section>

</body>
</html>
```